Clean Plinth Ads Banner Design For A Finance Company

Hi,
We're a UK based finance company and are looking for new banner ads to use on the Plinth Display Network.
We want the end product to stand out by using strong, minimal design - ideally starting from a dark theme, although I'm open to ideas.
The copy should read:
'Fast Bridging Loans From 0.39% PM'
Once we have these designs agreed, we are looking to replicate them for other products, changing only the text on each ad - for example, 'commercial mortgage service you can rely on' or 'development finance service you can rely on'.
The colours used on our website are the following:
Black - #040303
Orange - #f79124
White - #ffffff
Grey - #ffffff
Example ads that I like - https://www.brimcastle.com/wp-content/uploads/2021/07/plinth-display-ads-example-2-final.png.webp
2 - https://quendrahub.com/wp-content/uploads/2020/03/fbdd56ba3bd16c7a8debb13a411de786.jpg

```html
<!DOCTYPE html>
<html lang="en">
<head>
<meta charset="UTF-8">
<title>Bridging Loan Service Banner – Corvane Finance</title>
<link rel="stylesheet" href="https://fonts.googleapis.com/css2?family=Roboto+Slab:wght@400;500&display=swap">
<style>
  :root {
    --brand-orange: #f79124;
    --brand-black: #040303;
    --brand-white: #ffffff;
    --edge-brown: #4a2f1c;
    --photo-dark: #1f1815;
    --photo-wood: #3a2c26;
    --photo-teal: #5f9693;
    --photo-teal-deep: #3e6e6c;
    --headline-ink: #1b1512;
  }
  html, body {
    margin: 0;
    padding: 0;
    overflow: hidden;
    background: var(--brand-white);
  }
  .banner {
    position: relative;
    width: 1200px;
    height: 480px;
    overflow: hidden;
    background: var(--photo-dark);
  }
  .banner__photo {
    position: absolute;
    inset: 0;
    background:
      radial-gradient(ellipse 200px 230px at 820px 330px, var(--photo-teal) 0%, var(--photo-teal-deep) 55%, rgba(62,110,108,0) 100%),
      radial-gradient(ellipse 140px 60px at 470px 455px, rgba(150,115,60,0.55) 0%, rgba(150,115,60,0) 100%),
      radial-gradient(ellipse 90px 80px at 1000px 70px, rgba(220,190,175,0.55) 0%, rgba(220,190,175,0) 100%),
      linear-gradient(180deg, var(--photo-dark) 0%, var(--photo-wood) 60%, var(--photo-dark) 100%);
  }
  .banner__shapes {
    position: absolute;
    inset: 0;
  }
  .banner__headline {
    position: absolute;
    left: 17px;
    top: 132px;
    margin: 0;
    font-family: "Roboto Slab", serif;
    font-weight: 400;
    font-size: 31px;
    line-height: 45px;
    color: var(--headline-ink);
    white-space: nowrap;
  }
  .banner__brand {
    position: absolute;
    left: 16px;
    top: 376px;
    width: 192px;
    height: 91px;
    background: var(--brand-black);
    display: flex;
    align-items: center;
    justify-content: center;
  }
  .banner__brand-name {
    font-family: "Roboto Slab", serif;
    font-weight: 500;
    font-size: 20px;
    line-height: 1.15;
    color: var(--brand-white);
    text-align: center;
  }
</style>
</head>
<body>
  <div class="banner">
    <div class="banner__photo" role="img" aria-label="Photograph of a small teal wooden house labelled Bridging Loan, stacks of coins and a hand dropping a coin on a dark wooden background"></div>
    <svg class="banner__shapes" width="1200" height="480" viewBox="0 0 1200 480" aria-hidden="true">
      <polygon points="0,0 356,0 566,168 382,480 0,480" fill="var(--edge-brown)"/>
      <polygon points="0,0 348,0 556,168 372,480 0,480" fill="var(--brand-white)"/>
      <polygon points="0,0 336,0 542,168 360,480 0,480" fill="var(--brand-orange)"/>
    </svg>
    <h1 class="banner__headline">Bridging Loan Service<br>You Can Rely On<br>Think Corvane Finance</h1>
    <div class="banner__brand">
      <span class="banner__brand-name">Corvane<br>Finance Limited</span>
    </div>
  </div>
</body>
</html>
```